Stationery Design Project

I am looking to create stationary for our new airport valet company. I am looking for something modern and stylish.

i also want to have a faint picture of something in the background (like a hollogram) something related to valet.

Our company is called Brightmoor Valet & Concierge.
Updates

Reason: To Finalize the edits with the designer who has so far provided the total package of what we are looking for in stationary.

Target Market(s)

high end customers

Industry/Entity Type

Airport

Requirements
Must have
• 1. name of company
2. address
3. phone number (to be provided)
4. Brightmoor should be Black and Valet and Concierge should white
5. picture of valet or something relating to valet as a watermark on letterhead.

```html
<!DOCTYPE html>
<html lang="en">
<head>
<meta charset="utf-8">
<title>Brightmoor Valet &amp; Concierge – Business Card</title>
<link rel="stylesheet" href="https://fonts.googleapis.com/css2?family=Didact+Gothic&display=swap">
<style>
  :root {
    --backdrop: #e4e4e8;
    --card-white: #f4f5f7;
    --charcoal: #3a3a3b;
    --slate: #8c8e90;
    --ink: #3c3c3c;
    --paper: #ffffff;
  }
  * { margin: 0; padding: 0; box-sizing: border-box; }
  html, body {
    width: 1200px;
    height: 934px;
    overflow: hidden;
    background: var(--backdrop);
    font-family: "Didact Gothic", sans-serif;
  }
  .stage {
    position: relative;
    width: 1200px;
    height: 934px;
  }
  .card {
    position: absolute;
    width: 560px;
    height: 320px;
    overflow: hidden;
    box-shadow: 0 6px 18px rgba(0, 0, 0, 0.12);
  }
  /* Reverse side */
  .card--back {
    left: 90px;
    top: 150px;
    background: var(--charcoal);
    display: flex;
    align-items: center;
    justify-content: center;
  }
  .card--back .company-name {
    color: var(--paper);
    font-size: 24px;
    letter-spacing: 0.06em;
  }
  /* Front side */
  .card--front {
    left: 550px;
    top: 464px;
    background: var(--card-white);
  }
  .front-content {
    position: absolute;
    inset: 0 0 40px 0;
    display: flex;
    flex-direction: column;
    align-items: center;
    justify-content: center;
    gap: 34px;
  }
  .card--front .company-name {
    color: var(--ink);
    font-size: 28px;
    letter-spacing: 0.04em;
  }
  .contact {
    text-align: center;
    color: var(--ink);
    font-size: 14px;
    line-height: 1.6;
  }
  .contact .label { font-weight: 700; }
  .front-bands {
    position: absolute;
    left: 0;
    bottom: 0;
    width: 560px;
    height: 60px;
  }
</style>
</head>
<body>
  <main class="stage">
    <section class="card card--back" aria-label="Business card reverse">
      <p class="company-name">Brightmoor Valet &amp; Concierge</p>
    </section>

    <section class="card card--front" aria-label="Business card front">
      <div class="front-content">
        <p class="company-name">Brightmoor Valet &amp; Concierge</p>
        <address class="contact">
          4870 Harrowgate Lane<br>
          Kelsford, British Columbia, V9K 2M4<br>
          <span class="label">Tel:</span> 555.014.2276
        </address>
      </div>
      <svg class="front-bands" viewBox="0 0 560 60" aria-hidden="true">
        <polygon points="0,36 330,36 350,60 0,60" fill="var(--charcoal)"/>
        <polygon points="322,26 560,0 560,60 350,60 330,36" fill="var(--slate)"/>
      </svg>
    </section>
  </main>
</body>
</html>
```